International Trading Company, 'KIRO' needs a Business Card

The company name is "KIRO" and it has own logo design.
I'd like to use its logo on this business card.
I need two side Business Card.
I'll look forward to your great design.
Thank you very much in advance.

Contact Information for Business Card

Company Name : Kiro Harbour Limited
Information Example
Dorian Pallister
Mobile(use icon please) : 1 (212) 555-0143
Tel(use icon please) : 1 (212) 555-0178
Email(use icon please) : dorian27@kiroharbour-mail.com
Address(use icon please) : 482 Halden Ave, New York, NY 10160, USA

```html
<!DOCTYPE html>
<html lang="en">
<head>
<meta charset="utf-8">
<title>Kiro Harbour Limited — Business Card</title>
<link href="https://fonts.googleapis.com/css2?family=PT+Sans:wght@400;700&display=swap" rel="stylesheet">
<style>
  :root {
    --backdrop: #2b2b2b;
    --card-white: #f4f4f4;
    --card-edge: #e2e2e2;
    --pattern-light: #ececec;
    --pattern-mid: #d9d9d9;
    --band: #5b5b5b;
    --tab: #404040;
    --ink: #4a4a4a;
    --ink-soft: #7a7a7a;
    --on-dark: #ffffff;
  }
  * { margin: 0; padding: 0; box-sizing: border-box; }
  html, body { width: 1200px; height: 960px; overflow: hidden; }
  body {
    background: var(--backdrop);
    font-family: "PT Sans", "Helvetica Neue", Arial, sans-serif;
    position: relative;
  }
  .card {
    position: absolute;
    left: 250px;
    width: 700px;
    height: 400px;
    overflow: hidden;
    background: var(--card-white);
    box-shadow: 0 18px 40px rgba(0,0,0,.45);
  }
  .card--back { top: 60px; }
  .card--front { top: 500px; }

  /* back side */
  .back-texture {
    position: absolute; inset: 0;
    background: radial-gradient(ellipse at center, var(--pattern-light) 0%, var(--pattern-mid) 100%);
  }
  .back-wordmark {
    position: absolute; left: 0; right: 0; top: 120px;
    text-align: center;
    font-size: 130px; font-weight: 700; line-height: 1;
    color: var(--ink); letter-spacing: 4px;
  }
  .back-url {
    position: absolute; left: 0; right: 0; top: 290px;
    text-align: center;
    font-size: 17px; color: var(--ink-soft);
    letter-spacing: 7px;
  }

  /* front side */
  .front-shapes { position: absolute; inset: 0; }
  .front-wordmark {
    position: absolute; right: 40px; top: 60px;
    font-size: 104px; font-weight: 700; line-height: 1;
    color: var(--ink); letter-spacing: 4px;
  }
  .person { position: absolute; left: 28px; top: 156px; color: var(--on-dark); }
  .person__name { font-size: 20px; font-weight: 700; text-transform: uppercase; letter-spacing: .5px; line-height: 1.1; }
  .person__role { font-size: 16px; text-transform: uppercase; line-height: 1.3; }
  .contacts { position: absolute; left: 26px; top: 230px; list-style: none; color: var(--on-dark); }
  .contacts li { display: flex; align-items: center; gap: 10px; font-size: 17px; line-height: 24px; }
  .contacts svg { width: 14px; height: 14px; fill: var(--on-dark); flex: none; }
  .address {
    position: absolute; right: 32px; top: 318px;
    text-align: right; font-size: 18px; line-height: 23px;
    color: var(--ink-soft);
  }
</style>
</head>
<body>

  <section class="card card--back" aria-label="Business card, back side">
    <div class="back-texture" role="img" aria-label="Faint light grey decorative pattern across the card"></div>
    <div class="back-wordmark">KIRO</div>
    <div class="back-url">www.kiroharbour.com</div>
  </section>

  <section class="card card--front" aria-label="Business card, front side">
    <svg class="front-shapes" viewBox="0 0 700 400" width="700" height="400" aria-hidden="true">
      <polygon points="0,212 700,212 700,300 430,300 405,400 0,400" fill="var(--band)"/>
      <polygon points="0,145 268,145 305,205 0,205" fill="var(--tab)"/>
      <line x1="0" y1="208.5" x2="307" y2="208.5" stroke="#ffffff" stroke-width="2"/>
    </svg>

    <div class="front-wordmark">KIRO</div>

    <div class="person">
      <div class="person__name">Dorian Pallister</div>
      <div class="person__role">CEO/Founder</div>
    </div>

    <ul class="contacts">
      <li>
        <svg viewBox="0 0 24 24"><path d="M3 8c0-2 4-4 9-4s9 2 9 4v2h-5V8H8v2H3zM6 11h12l3 9H3z"/></svg>
        1 (212) 555-0178
      </li>
      <li>
        <svg viewBox="0 0 24 24"><path d="M7 1h10a2 2 0 0 1 2 2v18a2 2 0 0 1-2 2H7a2 2 0 0 1-2-2V3a2 2 0 0 1 2-2zm0 3v15h10V4zm5 16.2a1 1 0 1 0 0 .1z"/></svg>
        1 (212) 555-0143
      </li>
      <li>
        <svg viewBox="0 0 24 24"><path d="M2 5h20v14H2zm2 2v.4l8 5.6 8-5.6V7zm0 2.8V17h16V9.8l-8 5.6z"/></svg>
        dorian27@kiroharbour-mail.com
      </li>
      <li>
        <svg viewBox="0 0 24 24"><path d="M12 2a7 7 0 0 1 7 7c0 5-7 13-7 13S5 14 5 9a7 7 0 0 1 7-7zm0 4.5A2.5 2.5 0 1 0 12 11.5 2.5 2.5 0 0 0 12 6.5z"/></svg>
        www.kiroharbour.com
      </li>
    </ul>

    <address class="address" style="font-style: normal;">
      482 Halden Ave<br>
      New York<br>
      NY 10160, USA
    </address>
  </section>

</body>
</html>
```